Business Card for Lumina Nest

I need a very attractive business card as per the logo..

lumina nest is a centre providing services to pregnant women...

DR. Karim Haddadi

Consultant-  Maternal Fetal Medicine & Director of Lumina Nest Center

Kingdom of Saudi Arabia

Tel : +966 1 57 3 8164

Fax : +966 1 57 3 8275

khaddadi@luminanest.example

www.luminanest.example

Target Market(s)

the target market is the pregnant women and women having issues with pregnancy or with babies

Industry/Entity Type

Business

Requirements
Must have
• the business card will be in English and Arabic..........one we finalize the design maybe on the back u can place Arabic..of in the front one side may be Arabic one side english

```html
<!DOCTYPE html>
<html lang="en">
<head>
<meta charset="utf-8">
<title>Lumina Nest — Business Card</title>
<link rel="stylesheet" href="https://fonts.googleapis.com/css2?family=Exo+2:wght@400;600;700&family=Cairo:wght@500&display=swap">
<style>
  :root {
    --bg-top: #f1f2f3;
    --bg-bottom: #d9dadc;
    --card: #ffffff;
    --teal: #6fc8b9;
    --pink: #f29ca6;
    --ink: #2b2b2b;
    --white: #ffffff;
  }
  html, body {
    margin: 0;
    width: 1200px;
    height: 949px;
    overflow: hidden;
  }
  body {
    background: linear-gradient(180deg, var(--bg-top), var(--bg-bottom));
    font-family: "Exo 2", sans-serif;
    position: relative;
  }
  .card {
    position: absolute;
    left: 267px;
    width: 665px;
    height: 380px;
    border-radius: 22px;
    background: var(--card);
    box-shadow: 0 14px 30px rgba(0,0,0,0.18);
    overflow: hidden;
  }
  .card--front { top: 70px; }
  .card--back  { top: 500px; }
  .card svg { display: block; width: 665px; height: 380px; }

  .brand-dot { fill: var(--teal); }
  .brand-name { fill: var(--teal); font-size: 54px; font-weight: 400; }
  .brand-name--arabic { font-family: "Cairo", sans-serif; font-size: 24px; font-weight: 500; }

  .band { fill: var(--teal); }
  .badge { fill: var(--pink); }
  .badge-glyph { fill: var(--white); }
  .disc { fill: var(--white); }
  .disc-glyph { fill: var(--teal); }

  .person-name { fill: var(--ink); font-size: 20px; font-weight: 700; letter-spacing: 1.2px; }
  .person-role { fill: var(--ink); font-size: 8.5px; font-weight: 600; letter-spacing: 0.5px; }
  .detail { fill: var(--ink); font-size: 15px; font-weight: 600; letter-spacing: 0.5px; }
  .detail--light { fill: var(--white); font-size: 13px; font-weight: 400; }
</style>
</head>
<body>

  <section class="card card--front" aria-label="Card front">
    <svg viewBox="0 0 665 380">
      <circle class="brand-dot" cx="178" cy="182" r="30"/>
      <text class="brand-name" x="226" y="201">Lumina Nest</text>
      <text class="brand-name brand-name--arabic" x="332" y="262" text-anchor="middle" direction="rtl">لومينا نست</text>
    </svg>
  </section>

  <section class="card card--back" aria-label="Card back">
    <svg viewBox="0 0 665 380">
      <path class="band" d="M0 110 H275 V190 H665 V340 H0 Z"/>

      <!-- name -->
      <circle class="badge" cx="70" cy="30" r="15"/>
      <circle class="badge-glyph" cx="70" cy="25" r="4"/>
      <path class="badge-glyph" d="M62 38 a8 7 0 0 1 16 0 Z"/>
      <text class="person-name" x="32" y="68">DR. KARIM HADDADI</text>
      <text class="person-role" x="32" y="84">CONSULTANT - MATERNAL FETAL MEDICINE</text>
      <text class="person-role" x="32" y="97">&amp; DIRECTOR OF LUMINA NEST CENTER</text>

      <!-- address -->
      <circle class="badge" cx="350" cy="62" r="15"/>
      <path class="badge-glyph" d="M350 71 L344 61 a6 6 0 1 1 12 0 Z"/>
      <circle class="badge" cx="350" cy="58" r="2.2"/>
      <text class="detail" x="298" y="108">Kingdom of</text>
      <text class="detail" x="298" y="128">Saudi Arabia</text>

      <!-- phone -->
      <circle class="badge" cx="610" cy="100" r="15"/>
      <rect class="badge-glyph" x="605" y="91" width="10" height="18" rx="2"/>
      <rect class="badge" x="607" y="94" width="6" height="10"/>
      <text class="detail" x="640" y="150" text-anchor="end">Tel : +966 1 57 3 8164</text>
      <text class="detail" x="640" y="170" text-anchor="end">Fax : +966 1 57 3 8275</text>

      <!-- web -->
      <circle class="disc" cx="150" cy="165" r="26"/>
      <rect class="disc-glyph" x="137" y="154" width="26" height="17" rx="2"/>
      <rect class="disc" x="140" y="157" width="20" height="11"/>
      <rect class="disc-glyph" x="146" y="171" width="8" height="5"/>
      <text class="detail detail--light" x="40" y="226">khaddadi@luminanest.example</text>
      <text class="detail detail--light" x="40" y="246">www.luminanest.example</text>

      <!-- social -->
      <circle class="disc" cx="310" cy="220" r="14"/>
      <text class="detail detail--light" x="334" y="225">social.example/luminanest</text>
      <circle class="disc" cx="310" cy="258" r="14"/>
      <text class="detail detail--light" x="334" y="263">chirp.example/luminanest</text>
      <circle class="disc" cx="310" cy="296" r="14"/>
      <text class="detail detail--light" x="334" y="301">network.example/in/khaddadi</text>
    </svg>
  </section>

</body>
</html>
```